Buchcover für ein Glücksbuch
Zielgruppe
Ich brauche ein Cover für mein Glücksbuch, es soll möglichst viele interessierte Leser ansprechen und zum Kauf des Buches animieren.
Mein Glücksbuch ist für jeden gedacht, der auch im Alltag in kleinen Dingen sein Glück sucht, es muss nicht immer das große Glück sein und auch Geld allein macht nicht glücklich. Es soll den Leser dazu bringen, das Glück in sich selbt zu finden. Es enthält Anleitungen und Tipps und eine Bonus-Mediation.
Aufgabenstellung
Der Titel des Buches lautet: 'Pfade zur Freude mit 12 Herzensfunken'
Untertitel: 'Heiter und gelassen jeden Tag mit Ideen und Übungen'
'Mit Bonus-Meditation'
Autorin (Pseudonym): Britta Wolder

```html
<!DOCTYPE html>
<html lang="de">
<head>
<meta charset="utf-8">
<title>Pfade zur Freude mit 12 Herzensfunken – Buchcover</title>
<link rel="stylesheet" href="https://fonts.googleapis.com/css2?family=Petit+Formal+Script&family=Oswald:wght@500&family=Poppins:wght@300&display=swap">
<style>
  :root {
    --teal-deep: #1f6163;
    --teal-mid: #2f7f80;
    --teal-soft: #6aa9ad;
    --panel: #2a6b6a;
    --spine: #276566;
    --badge: #1c5557;
    --ladybug: #d8342b;
    --white: #ffffff;
    --ink-light: #f4fbfb;
  }
  * { margin: 0; padding: 0; box-sizing: border-box; }
  html, body { width: 1200px; height: 833px; overflow: hidden; background: var(--teal-deep); }
  .cover {
    position: relative; width: 1200px; height: 833px; overflow: hidden;
    background: linear-gradient(160deg, var(--teal-mid) 0%, var(--teal-deep) 60%, #246b6c 100%);
  }
  .cover-photo {
    position: absolute; left: 360px; top: 0; width: 840px; height: 833px;
    background:
      radial-gradient(ellipse 180px 120px at 880px 440px, rgba(200,70,50,0.35), transparent 70%),
      radial-gradient(ellipse 260px 300px at 500px 420px, rgba(205,230,233,0.75), transparent 70%),
      radial-gradient(ellipse 260px 320px at 780px 470px, rgba(190,222,226,0.7), transparent 70%),
      radial-gradient(ellipse 200px 260px at 200px 520px, rgba(180,215,220,0.55), transparent 70%),
      linear-gradient(90deg, rgba(47,127,128,0) 0%, var(--teal-soft) 30%, var(--teal-soft) 100%);
  }
  .blurb-panel {
    position: absolute; left: 115px; top: 127px; width: 311px; height: 509px;
    background: var(--panel);
  }
  .author-photo {
    position: absolute; left: 42px; top: 99px; width: 170px; height: 216px;
    background: linear-gradient(180deg, #c9c9c6 0%, #b7b8b4 45%, #2f6e3f 46%, #1f5a33 100%);
  }
  .blurb {
    position: absolute; font-family: "Poppins", sans-serif; font-weight: 300;
    font-size: 10.4px; line-height: 15.65px; letter-spacing: -0.4px; color: var(--ink-light);
  }
  .blurb .line {
    display: block; white-space: nowrap;
    text-align: justify; text-align-last: justify;
  }
  .blurb .line.end { text-align: left; text-align-last: left; }
  .blurb-para + .blurb-para { margin-top: 4px; }
  .blurb-intro { left: 228px; top: 187px; width: 179px; }
  .blurb-main { left: 139px; top: 329px; width: 268px; }
  .spine {
    position: absolute; left: 557px; top: 0; width: 62px; height: 833px;
    background: var(--spine);
  }
  .spine-title {
    position: absolute; left: 31px; top: 443px; white-space: nowrap;
    transform: translate(-50%, -50%) rotate(-90deg);
    font-family: "Petit Formal Script", cursive; font-size: 26px; color: var(--white);
    letter-spacing: 1px;
  }
  .title-line {
    position: absolute; font-family: "Petit Formal Script", cursive; color: var(--white);
    font-size: 64px; font-weight: 400; line-height: 1; white-space: nowrap; letter-spacing: 2px;
  }
  .t1 { left: 700px; top: 28px; }
  .t2 { left: 650px; top: 108px; }
  .t3 { left: 695px; top: 178px; font-size: 70px; }
  .t4 { left: 650px; top: 262px; }
  .author {
    position: absolute; left: 648px; top: 326px;
    font-family: "Oswald", sans-serif; font-weight: 500; font-size: 36px; line-height: 44px;
    color: var(--white);
  }
  .subtitle {
    position: absolute; left: 650px; top: 706px; width: 536px; text-align: center;
    font-family: "Oswald", sans-serif; font-weight: 500; font-size: 33px; line-height: 44px;
    color: var(--white); letter-spacing: 1.2px; text-shadow: 0 1px 3px rgba(0,40,40,0.45);
    white-space: nowrap;
  }
  .badge { position: absolute; left: 1052px; top: 556px; width: 150px; height: 150px; }
</style>
</head>
<body>
<div class="cover">
  <div class="cover-photo" role="img" aria-label="Foto: Marienkäfer auf den Samenschirmen einer Pusteblume vor türkisem Hintergrund"></div>

  <div class="blurb-panel"></div>
  <div class="author-photo" role="img" aria-label="Porträtfoto der Autorin in grüner Bluse vor hellgrauer Wand"></div>

  <div class="blurb blurb-intro">
    <p class="blurb-para">
      <span class="line">In den 25 Jahren meiner selbstän-</span>
      <span class="line">digen Arbeit als Hebamme, habe</span>
      <span class="line">ich viele Familien im Wochenbett</span>
      <span class="line">betreut und dabei einen reichen</span>
      <span class="line">Erfahrungsschatz gesammelt.</span>
      <span class="line">Meine häufigsten Kunden waren</span>
      <span class="line">natürlich Familien, die das erste</span>
      <span class="line end">Kind bekommen haben.</span>
    </p>
  </div>

  <div class="blurb blurb-main">
    <p class="blurb-para">
      <span class="line">Dies war zu der Zeit, als gerade der Krankenhaus-</span>
      <span class="line">aufenthalt nach einer Spontangeburt von zehn</span>
      <span class="line">auf sieben Tage gekürzt worden war. Die Kran-</span>
      <span class="line">kenkasse bezahlte im Anschluss daran vier Tage</span>
      <span class="line">Hebammen- Betreuung. Wenn die Familie diver-</span>
      <span class="line">se schwierige Themenfelder hatte, übernahm die</span>
      <span class="line end">Kasse die Kosten auch länger.</span>
    </p>
    <p class="blurb-para">
      <span class="line">Da ich meinen Beruf liebte, nahm ich mir für den</span>
      <span class="line">Wochenbettbesuch auch immer genügend Zeit.</span>
      <span class="line">Meist war eine Stunde nötig, manchmal jedoch</span>
      <span class="line">waren so viele Fragen oder Irritationen (Unklar-</span>
      <span class="line">heiten), daß ich länger blieb. Auf die frisch geba-</span>
      <span class="line">ckenen Eltern kommen unzählige unbekannte Si-</span>
      <span class="line">tuationen zu, die total verunsichern können. Auch</span>
      <span class="line">bei sehr einfühlsamer Betreuung im Krankenhaus</span>
      <span class="line">stellen sich viele Fragen erst zu Hause. Nämlich</span>
      <span class="line end">dann, wenn der Alltag mit dem Baby beginnt.</span>
    </p>
  </div>

  <div class="spine">
    <div class="spine-title">Pfade zur Freude mit 12 Herzens- funken</div>
  </div>

  <h1>
    <span class="title-line t1">Pfade zur</span>
    <span class="title-line t2">Freude mit</span>
    <span class="title-line t3">12 Herzens-</span>
    <span class="title-line t4">funken</span>
  </h1>
  <div class="author">Britta Wolder</div>

  <svg class="badge" viewBox="0 0 150 150" aria-label="Mit Bonus-Meditation">
    <defs>
      <path id="badge-arc" d="M 47 26.5 A 56 56 0 1 0 103 26.5"/>
    </defs>
    <circle cx="75" cy="75" r="74" fill="var(--badge)"/>
    <text font-family="Oswald, sans-serif" font-weight="500" font-size="21" fill="var(--white)" letter-spacing="1.5" text-anchor="middle">
      <textPath href="#badge-arc" startOffset="50%">Mit Bonus-Meditation</textPath>
    </text>
    <circle cx="75" cy="68" r="21" fill="var(--ladybug)" role="img" aria-label="Illustration: kleiner Marienkäfer"/>
  </svg>

  <div class="subtitle">Heiter und gelassen jeden Tag<br>mit Ideen und Übungen</div>
</div>
</body>
</html>
```